Awesome Redesign of Plumbing website

A great website designer to create this page for us in Wordpress with elementor.

- You are redesigning this site: http://fjellbekkror.no/

- Brand name is : Vannlinje Nord

- You can take pictures from the website or the one i attach, or stock images or AI generated images etc.

- The main call to action is to call the phone number (+47 23 86 51 94)
So please make that a priority.
- Mobile responsiveness is very important.
- The background should be white. You can use the color code red, white and black when you create the site.

I want you to build the website with a high speed score.

Target Market(s)

Residential market in oslo, Norway

Industry/Entity Type

Plumbing

Coding

Coded - Design and coding required

Requirements
Must have
• Build with elementor (wordpress), SEO friendly, A good CTA for phone, mobile responsive. Fast loading time. A Clean design.
Should not have
• Stock images that look "fake". All pictures have an authentic feel.

```html
<!DOCTYPE html>
<html lang="no">
<head>
<meta charset="utf-8">
<title>Vannlinje Nord – Rørlegger</title>
<link href="https://fonts.googleapis.com/css2?family=Montserrat:wght@600;700;800&family=Poppins:wght@400;500;600&display=swap" rel="stylesheet">
<style>
:root{
  --teal:#3f8f8b;
  --teal-dark:#2f6f6c;
  --teal-soft:rgba(63,143,139,.82);
  --ink:#141414;
  --text:#3a3a3a;
  --muted:#8a8f92;
  --line:#e3e7e8;
  --white:#ffffff;
  --pale:#eef4f6;
  --star:#f5b400;
}
*{box-sizing:border-box;margin:0;padding:0}
html,body{width:1200px;height:3871px;overflow:hidden;background:var(--white)}
body{position:relative;font-family:"Poppins",sans-serif;color:var(--text)}
.abs{position:absolute}
.heading{font-family:"Montserrat",sans-serif;font-weight:700;color:var(--ink);letter-spacing:1.5px;text-transform:uppercase}
.center{left:0;width:1200px;text-align:center}
.btn{position:absolute;display:flex;align-items:center;justify-content:center;border-radius:30px;font-family:"Montserrat",sans-serif;font-weight:700;font-size:11px;letter-spacing:.5px;text-transform:uppercase}

/* hero */
.hero{left:0;top:0;width:1200px;height:690px;background:linear-gradient(100deg,#2b2d2c 0%,#3d403e 45%,#2f3332 100%);overflow:hidden}
.hero-photo{left:0;top:0;width:1200px;height:690px;background:radial-gradient(ellipse at 45% 35%,rgba(120,120,112,.45),transparent 60%)}
.header-brand{left:148px;top:18px;width:100px;display:flex;flex-direction:column;align-items:center;gap:5px;color:var(--white);font-family:"Montserrat",sans-serif;font-weight:700;font-size:10px;letter-spacing:1px;text-transform:uppercase;white-space:nowrap}
.header-brand .dot{width:30px;height:30px;border:2px solid currentColor;border-radius:50%}
.nav a{position:absolute;top:36px;color:var(--white);font-family:"Montserrat",sans-serif;font-weight:600;font-size:11px;text-decoration:none}
.call-label{left:947px;top:24px;color:var(--white);font-family:"Montserrat",sans-serif;font-weight:700;font-size:12px;line-height:17px}
.call-label span{font-size:14px}
.hero-title{left:146px;top:266px;font-family:"Montserrat",sans-serif;font-weight:800;font-size:47px;line-height:48px;color:var(--white);letter-spacing:1px}
.hero-sub{left:149px;top:382px;color:var(--white);font-size:14.5px;letter-spacing:.3px}
.form-panel{left:641px;top:190px;width:418px;height:370px;background:var(--teal-soft)}
.form-frame{left:7px;top:13px;width:397px;height:345px;border:2px solid var(--white)}
.form-title{left:0;top:40px;width:418px;text-align:center;color:var(--white);font-size:23px;line-height:31px;font-weight:500}
.form-note{left:0;top:108px;width:418px;text-align:center;color:var(--white);font-size:13px;letter-spacing:.3px}
.field{position:absolute;left:48px;width:316px;height:43px;background:var(--white);border-radius:22px;font-family:"Montserrat",sans-serif;font-weight:700;font-size:11px;color:var(--ink);padding-left:20px;display:flex;align-items:center}

/* partners */
.partners-title{top:810px;font-family:"Montserrat",sans-serif;font-weight:700;font-size:17px;letter-spacing:1px;color:var(--ink)}
.rule{height:1px;background:var(--line)}
.badge{background:#cfd5d7;border-radius:6px}

/* services */
.services-bg{left:0;top:990px;width:1200px;height:430px;background:linear-gradient(#fff,var(--pale))}
.section-title{font-size:37px}
.sub{font-size:14px;letter-spacing:.3px;color:var(--text)}
.card{position:absolute;top:1160px;width:161px;height:180px;background:var(--white);box-shadow:0 6px 18px rgba(40,70,80,.1)}
.card svg{position:absolute;left:50%;top:35px;transform:translateX(-50%)}
.card p{position:absolute;left:0;bottom:34px;width:100%;text-align:center;font-family:"Montserrat",sans-serif;font-weight:700;font-size:14px;line-height:17px;color:var(--ink)}

/* why */
.photo{background:linear-gradient(135deg,#5b5c5b,#8d8e8a)}
.why-item{position:absolute;left:688px;width:345px;height:44px;border-bottom:1px solid var(--line);display:flex;align-items:center;gap:9px;font-size:14px;color:var(--ink);letter-spacing:.3px}

/* cta panels */
.cta{top:2020px;width:600px;height:460px}
.boxed{position:absolute;border:2px solid var(--white);color:var(--white);font-family:"Montserrat",sans-serif;font-weight:700;font-size:20px;letter-spacing:1.5px;display:flex;align-items:center;justify-content:center}
.cta-text{position:absolute;left:0;width:600px;text-align:center;color:var(--white);font-family:"Montserrat",sans-serif;font-weight:700;font-size:20px;line-height:28px;letter-spacing:1.3px}
.btn.white{background:var(--white);color:var(--teal)}

/* reviews */
.review{position:absolute;top:2740px;width:276px;height:325px;background:var(--white);box-shadow:0 6px 22px rgba(40,70,80,.1)}
.review h3{position:absolute;left:26px;top:86px;font-family:"Montserrat",sans-serif;font-weight:700;font-size:18px;color:var(--teal-dark)}
.review p{position:absolute;left:26px;top:118px;width:232px;font-size:11px;line-height:22.5px;color:var(--text)}
.avatar{position:absolute;left:26px;top:258px;width:48px;height:48px;background:linear-gradient(135deg,#6f7b82,#b5bcc0)}
.reviewer{position:absolute;left:85px;top:262px;font-family:"Montserrat",sans-serif;font-weight:700;font-size:11px;color:var(--teal-dark)}
.mini-stars{position:absolute;left:85px;top:280px;color:var(--star);font-size:12px;letter-spacing:3px}

/* contact band */
.contact-band{left:0;top:3170px;width:1200px;height:360px;background:linear-gradient(90deg,#3a8985,#4b9792 60%,#3d8a86)}

/* footer */
.footer-brand{left:148px;top:3618px;display:flex;align-items:center;gap:8px;color:var(--ink);font-family:"Montserrat",sans-serif;font-weight:700;font-size:18px;letter-spacing:1.5px;white-space:nowrap}
.footer-brand .dot{width:50px;height:50px;border:2px solid var(--teal);border-radius:50%}
.foot-h{font-family:"Montserrat",sans-serif;font-weight:600;font-size:12px;color:var(--ink)}
.foot-link{position:absolute;font-family:"Montserrat",sans-serif;font-weight:600;font-size:9.5px;color:var(--ink)}
.foot-p{font-family:"Montserrat",sans-serif;font-weight:600;font-size:10px;line-height:20px;color:var(--ink)}
.social{position:absolute;top:3625px;width:23px;height:23px;border-radius:50%;background:var(--ink)}
</style>
</head>
<body>

<!-- Hero -->
<section class="abs hero">
  <div class="abs hero-photo" role="img" aria-label="Dark modern bathroom with wooden panels, round mirror and vanity"></div>
  <div class="abs header-brand"><span class="dot"></span>Vannlinje Nord</div>
  <nav class="nav">
    <a style="left:270px">Home</a>
    <a style="left:337px">Services</a>
    <a style="left:417px">About</a>
    <a style="left:485px">Environment</a>
  </nav>
  <div class="btn" style="left:778px;top:23px;width:102px;height:38px;background:var(--teal);color:var(--white);text-transform:none;font-weight:600">Contact</div>
  <svg class="abs" style="left:897px;top:22px" width="40" height="40" viewBox="0 0 40 40">
    <circle cx="20" cy="20" r="20" fill="#fff"/>
    <path d="M14 12c1-1 2-1 3 0l2 3c.5 1 0 2-1 2.5 1 2 2.5 3.5 4.5 4.5.5-1 1.5-1.5 2.5-1l3 2c1 1 1 2 0 3l-1.5 1.5c-5 0-13-8-13-13z" fill="none" stroke="var(--teal)" stroke-width="1.6"/>
  </svg>
  <div class="abs call-label">Call Us Now<br><span>+47 23 86 51 94</span></div>

  <h1 class="abs hero-title">RORSERVICE<br>PLUMBER OSLO</h1>
  <p class="abs hero-sub">Vi hjelper deg med alt arbeid relatert til Rørlegging.</p>
  <div class="btn" style="left:150px;top:430px;width:172px;height:43px;background:var(--teal);color:var(--white);font-size:10.5px">Ring nå 23 86 51 94</div>

  <div class="abs form-panel">
    <div class="abs form-frame"></div>
    <p class="abs form-title">Fill out the non-binding form,<br>get an answer today!</p>
    <p class="abs form-note">(The form takes a few seconds to fill out)</p>
    <div class="field" style="top:156px">Oslo
      <svg style="position:absolute;right:20px;top:15px" width="13" height="13" viewBox="0 0 13 13"><circle cx="6.5" cy="6.5" r="5.5" fill="none" stroke="var(--teal)"/><path d="M4 6.5l2 2 3-3.5" fill="none" stroke="var(--teal)"/></svg>
    </div>
    <div class="field" style="top:210px">Utenfor Oslo</div>
    <div class="btn" style="left:121px;top:274px;width:171px;height:44px;background:#0f0f0f;color:var(--white);font-size:10.5px">Ring nå 23 86 51 94</div>
  </div>

  <svg class="abs" style="left:0;top:600px" width="1200" height="90" viewBox="0 0 1200 90">
    <path d="M0 28 Q600 140 1200 28 L1200 90 L0 90 Z" fill="#fff"/>
  </svg>
</section>

<!-- Partners -->
<div class="abs rule" style="left:148px;top:820px;width:357px"></div>
<div class="abs rule" style="left:695px;top:820px;width:365px"></div>
<h2 class="abs center partners-title">OUR PARTNERS</h2>
<div class="abs badge" style="left:150px;top:875px;width:94px;height:36px"></div>
<div class="abs badge" style="left:303px;top:866px;width:54px;height:54px;border-radius:50%"></div>
<div class="abs badge" style="left:415px;top:868px;width:92px;height:48px"></div>
<div class="abs badge" style="left:566px;top:875px;width:94px;height:36px"></div>
<div class="abs badge" style="left:722px;top:862px;width:62px;height:62px;background:#1a1a1a"></div>
<div class="abs badge" style="left:846px;top:860px;width:64px;height:66px;background:#c9b27a"></div>
<div class="abs badge" style="left:970px;top:868px;width:92px;height:48px"></div>

<!-- Services -->
<div class="abs services-bg"></div>
<h2 class="abs center heading section-title" style="top:1045px">A few selected services</h2>
<p class="abs center sub" style="top:1103px">Vi hjelper deg med alt arbeid relatert til Rørlegging,</p>

<div class="card" style="left:148px">
  <svg width="44" height="56" viewBox="0 0 44 56" fill="none" stroke="var(--teal)" stroke-width="2"><rect x="2" y="4" width="40" height="50"/><path d="M2 14h40M20 14v40M8 8h4"/></svg>
  <p>Wet<br>Room</p>
</div>
<div class="card" style="left:333px">
  <svg width="60" height="58" viewBox="0 0 60 58" fill="none" stroke="var(--teal)" stroke-width="2"><path d="M10 2h12v8h-4v22a10 10 0 0 0 20 0v-6h8v-6h8v20h-8v-6h-2a18 18 0 0 1-34 0V10h-4V2"/></svg>
  <p>Clogged<br>Drain Pipes</p>
</div>
<div class="card" style="left:518px">
  <svg width="42" height="58" viewBox="0 0 42 58" fill="none" stroke="var(--teal)" stroke-width="2"><rect x="2" y="2" width="38" height="54" rx="8"/><path d="M10 12h22"/><circle cx="21" cy="36" r="9"/><path d="M21 31c-2 3-3 5 0 8 3-3 2-5 0-8z"/></svg>
  <p>Heat<br>Pumps</p>
</div>
<div class="card" style="left:703px">
  <svg width="60" height="58" viewBox="0 0 60 58" fill="none" stroke="var(--teal)" stroke-width="2"><path d="M2 8l16 4-4 12L2 20zM58 8l-16 4 4 12 12-4zM18 12l24 0M14 24l32 0"/><path d="M30 30c-2 4-3 6 0 9 3-3 2-5 0-9zM20 36v3M40 36v3M26 48v3M34 48v3"/></svg>
  <p>Water<br>Leakage</p>
</div>
<div class="card" style="left:888px">
  <svg width="62" height="58" viewBox="0 0 62 58" fill="none" stroke="var(--teal)" stroke-width="2"><circle cx="31" cy="14" r="12"/><path d="M31 14l5-6M31 26v8M2 36h58v14H2zM20 34h22v18H20z"/></svg>
  <p>Pressure<br>Reducing Valve</p>
</div>

<!-- Why choose -->
<svg class="abs" style="left:220px;top:1520px" width="380" height="360" viewBox="0 0 380 360" fill="none" stroke="#e4eeee" stroke-width="3">
  <circle cx="190" cy="180" r="160"/>
</svg>
<div class="abs photo" style="left:163px;top:1505px;width:267px;height:260px;background:linear-gradient(135deg,#3f4040,#7a7b78 60%,#5a5a58)" role="img" aria-label="Bathroom with double washbasins on a dark wooden vanity"></div>
<div class="abs" style="left:342px;top:1640px;width:250px;height:244px;background:#fff"></div>
<div class="abs photo" style="left:348px;top:1648px;width:240px;height:232px;background:linear-gradient(180deg,#b9bdbf,#6c7073 45%,#222 100%)" role="img" aria-label="Two plumbers in dark company shirts standing outside"></div>

<h2 class="abs heading" style="left:688px;top:1514px;font-size:37px;line-height:47px">Why choose<br>Oslo plumbing?</h2>
<div class="why-item" style="top:1628px"><svg width="12" height="12" viewBox="0 0 12 12"><circle cx="6" cy="6" r="5" fill="none" stroke="var(--teal)"/><path d="M3.5 6l1.8 1.8L8.5 4.5" fill="none" stroke="var(--teal)"/></svg>Non-binding and reasonable prices</div>
<div class="why-item" style="top:1672px"><svg width="12" height="12" viewBox="0 0 12 12"><circle cx="6" cy="6" r="5" fill="none" stroke="var(--teal)"/><path d="M3.5 6l1.8 1.8L8.5 4.5" fill="none" stroke="var(--teal)"/></svg>Always fixed price</div>
<div class="why-item" style="top:1716px"><svg width="12" height="12" viewBox="0 0 12 12"><circle cx="6" cy="6" r="5" fill="none" stroke="var(--teal)"/><path d="M3.5 6l1.8 1.8L8.5 4.5" fill="none" stroke="var(--teal)"/></svg>Punctual arrival</div>
<div class="why-item" style="top:1760px"><svg width="12" height="12" viewBox="0 0 12 12"><circle cx="6" cy="6" r="5" fill="none" stroke="var(--teal)"/><path d="M3.5 6l1.8 1.8L8.5 4.5" fill="none" stroke="var(--teal)"/></svg>Only certified and trained plumbers</div>
<div class="why-item" style="top:1803px"><svg width="12" height="12" viewBox="0 0 12 12"><circle cx="6" cy="6" r="5" fill="none" stroke="var(--teal)"/><path d="M3.5 6l1.8 1.8L8.5 4.5" fill="none" stroke="var(--teal)"/></svg>Competitive prices</div>
<div class="why-item" style="top:1847px;border-bottom:none"><svg width="12" height="12" viewBox="0 0 12 12"><circle cx="6" cy="6" r="5" fill="none" stroke="var(--teal)"/><path d="M3.5 6l1.8 1.8L8.5 4.5" fill="none" stroke="var(--teal)"/></svg>Job done right the first time</div>

<!-- CTA panels -->
<section class="abs cta" style="left:0;background:linear-gradient(180deg,#3d7e80,#2f6b70 60%,#3f8a88)" role="img" aria-label="Company service van parked by a forest">
  <div class="boxed" style="left:275px;top:143px;width:200px;height:38px">OUR PLUMBING</div>
  <p class="cta-text" style="top:198px;left:-26px">COMPANY IN OSLO OFFERS GOOD &amp;<br>AFFORDABLE PLUMBING HELP</p>
  <div class="btn white" style="left:290px;top:271px;width:170px;height:42px;font-size:10.5px">Ring nå 23 86 51 94</div>
</section>
<section class="abs cta" style="left:600px;background:linear-gradient(180deg,#5ea39f,#4b918d 60%,#4f9894)" role="img" aria-label="Bright bathroom with glass shower and tiles">
  <div class="boxed" style="left:173px;top:143px;width:141px;height:38px">CALL FOR</div>
  <p class="cta-text" style="top:198px;left:-6px">ALL NEEDS - CHEAP EMERGENCY<br>PLUMBING HELP</p>
  <div class="btn white" style="left:160px;top:271px;width:170px;height:42px;font-size:10.5px">Ring nå 23 86 51 94</div>
</section>
<svg class="abs" style="left:0;top:2350px" width="1200" height="135" viewBox="0 0 1200 135">
  <path d="M0 40 Q600 230 1200 20 L1200 135 L0 135 Z" fill="#fff"/>
</svg>

<!-- Reviews -->
<h2 class="abs center heading section-title" style="top:2569px">Long experience you can trust</h2>
<p class="abs center sub" style="top:2628px">Vi hjelper deg med alt arbeid relatert til Rørlegging,</p>
<div class="abs center" style="top:2666px;font-size:19px;color:var(--ink)"><span style="color:var(--star);font-size:30px;letter-spacing:2px;vertical-align:-3px">★★★★★</span> <b style="font-weight:600">4.8</b> (278 evalueringer)</div>

<div class="review" style="left:148px">
  <svg style="position:absolute;left:26px;top:28px" width="42" height="36" viewBox="0 0 42 36" fill="none" stroke="var(--teal)" stroke-width="2"><path d="M2 34V16C2 8 7 3 16 2v6c-5 1-7 4-7 8h7v18zM24 34V16c0-8 5-13 14-14v6c-5 1-7 4-7 8h7v18z"/></svg>
  <h3>Lorem Ipsum dollar</h3>
  <p>"It is a long established fact that a reader will be distracted by the readable content of a page when looking at its layout. The point of using Lorem Ipsum is that it has a more-or-less normal opposed"</p>
  <div class="avatar" role="img" aria-label="Customer portrait"></div>
  <div class="reviewer">ERIK LUNDE</div>
  <div class="mini-stars">★★★★★</div>
</div>
<div class="review" style="left:462px">
  <svg style="position:absolute;left:26px;top:28px" width="42" height="36" viewBox="0 0 42 36" fill="none" stroke="var(--teal)" stroke-width="2"><path d="M2 34V16C2 8 7 3 16 2v6c-5 1-7 4-7 8h7v18zM24 34V16c0-8 5-13 14-14v6c-5 1-7 4-7 8h7v18z"/></svg>
  <h3>Lorem Ipsum dollar</h3>
  <p>"It is a long established fact that a reader will be distracted by the readable content of a page when looking at its layout. The point of using Lorem Ipsum is that it has a more-or-less normal opposed"</p>
  <div class="avatar" role="img" aria-label="Customer portrait"></div>
  <div class="reviewer">ERIK LUNDE</div>
  <div class="mini-stars">★★★★★</div>
</div>
<div class="review" style="left:776px">
  <svg style="position:absolute;left:26px;top:28px" width="42" height="36" viewBox="0 0 42 36" fill="none" stroke="var(--teal)" stroke-width="2"><path d="M2 34V16C2 8 7 3 16 2v6c-5 1-7 4-7 8h7v18zM24 34V16c0-8 5-13 14-14v6c-5 1-7 4-7 8h7v18z"/></svg>
  <h3>Lorem Ipsum dollar</h3>
  <p>"It is a long established fact that a reader will be distracted by the readable content of a page when looking at its layout. The point of using Lorem Ipsum is that it has a more-or-less normal opposed"</p>
  <div class="avatar" role="img" aria-label="Customer portrait"></div>
  <div class="reviewer">ERIK LUNDE</div>
  <div class="mini-stars">★★★★★</div>
</div>

<!-- Contact band -->
<section class="abs contact-band" role="img" aria-label="Service van on a street behind a teal overlay"></section>
<svg class="abs" style="left:0;top:3410px" width="1200" height="125" viewBox="0 0 1200 125">
  <path d="M0 35 Q600 170 1200 25 L1200 125 L0 125 Z" fill="#fff"/>
</svg>
<h2 class="abs center heading" style="top:3240px;font-size:37px;line-height:47px;color:var(--white)">Please contact us<br>for an informal chat</h2>
<p class="abs center sub" style="top:3346px;color:var(--white)">Vi hjelper deg med alt arbeid relatert til Rørlegging,</p>
<div class="btn" style="left:482px;top:3395px;width:235px;height:43px;background:#111;color:var(--white);font-size:10.5px">Ring oss nå +47 23 86 51 94</div>
<svg class="abs" style="left:730px;top:3360px" width="110" height="60" viewBox="0 0 110 60" fill="none" stroke="#fff" stroke-width="1.5">
  <path d="M100 4c8 14-6 28-20 24-6-2-2-10 4-6 6 6-10 24-76 24"/><path d="M14 44l-8 6 8 5"/>
</svg>

<!-- Footer -->
<footer>
  <div class="abs footer-brand"><span class="dot"></span>VANNLINJE NORD</div>
  <p class="abs foot-p" style="left:148px;top:3676px;width:240px">It is a long established fact that a reader will be distracted by the readable content of a page when looking at its layout. The point of using Lorem Ipsum dummy text.</p>

  <h4 class="abs foot-h" style="left:440px;top:3628px">Navigation</h4>
  <span class="foot-link" style="left:440px;top:3675px">Fire protection</span>
  <span class="foot-link" style="left:440px;top:3701px">Industry</span>
  <span class="foot-link" style="left:440px;top:3727px">Service &amp; Maintenance</span>
  <span class="foot-link" style="left:440px;top:3753px">Plumber on duty</span>
  <span class="foot-link" style="left:440px;top:3779px">Refurbishing a bathroom in oslo</span>
  <span class="foot-link" style="left:620px;top:3675px">Heat pump</span>
  <span class="foot-link" style="left:620px;top:3701px">Radiator</span>
  <span class="foot-link" style="left:620px;top:3727px">Clean pipes oslo</span>
  <span class="foot-link" style="left:620px;top:3753px">Pipe inspection</span>

  <h4 class="abs foot-h" style="left:778px;top:3628px">Resources</h4>
  <span class="foot-link" style="left:778px;top:3675px">Support</span>
  <span class="foot-link" style="left:778px;top:3701px">Contact</span>
  <span class="foot-link" style="left:778px;top:3727px">Privacy &amp; terms</span>
  <span class="foot-link" style="left:778px;top:3753px">Sitemap</span>

  <span class="social" style="left:926px"></span>
  <span class="social" style="left:966px"></span>
  <span class="social" style="left:1007px"></span>
  <p class="abs" style="left:880px;top:3675px;width:182px;text-align:right;font-size:13px;color:var(--teal)">post@vannlinjenord.no</p>
  <p class="abs" style="left:880px;top:3700px;width:152px;text-align:right;font-size:13px;color:var(--teal)">+47 400 18 272</p>
</footer>

</body>
</html>
```